Prairie Wellhead Gear Depot Web Template
Oilfield Equipment web site development
Also #76 shows off shore ...........
thanks,
CraftyPixelSmith
ZorbIx
Hi PH,
please feel free to let me know the required changes so that your expectations are met.
Awaiting for your kind feedback
Designers: Thank you for all of your submitted drafts. The few that remain on the page are what I am look for in terms of a home page. Please keep the designs coming, I really appreciate all of your hard work. Everything looks great so far. I would like to keep the images land related. Ex: no offshore rig pictures. Our targeted area is for onshore production not offshore.
DRAFT # 9 IS AN EXAMPLE OF THE TYPE OF HOME PAGE TEMPLATE I AM LOOKING FOR.
NOTE: PRAIRIE WELLHEAD GEAR DEPOT IS SINGULAR. THE WORD EQUIPMENT SHOULD NEVER HAVE AN "S" AT THE END OF THE WORD. EX: DRAFTS # 4-9 SHOULD NOT HAVE A "S" AT THE END OF EQUIPMENT IN "WELCOME TO PRAIRIE WELLHEAD GEAR(S) DEPOT". ALSO IN "FEATURED EQUIPMENT(S).
Just a thought.....I would like to have the ability to show the current crude oil prices shown in a graph that is updated daily. Ex: www.barrel-rates-demo.net
I would like the logo to be larger than in Drafts #1-3.
Icon "equipment for sale" is singular and not plural
The website will be strictly to advertise equipment for sale and customers will not be able to purchase equipment through a shopping cart.
In drafts # 1-3, lets change "featured articles" to "featured equipment".
Website template should have 5 icons.
1st icon: home
2nd icon: about us
3rd icon: services
4th icon: equipment for sale
5th icon: contact us
Quick reminder:
I would like to keep “offshore rig pictures” off the home page. The equipment that is being sold is for the oil and gas industry but mainly used onshore in the production side of things.
I like the clean lines on draft #1. Draft # 1 is definitely on the right track. Keep up the good work. I look forward to seeing everyone’s drafts.

```html
<!DOCTYPE html>
<html lang="en">
<head>
<meta charset="utf-8">
<title>Prairie Wellhead Gear Depot</title>
<link rel="stylesheet" href="https://fonts.googleapis.com/css2?family=Arimo:wght@400;700&display=swap">
<style>
:root{
  --red:#c4161c;
  --red-dark:#8e0d12;
  --ink:#222;
  --bg:#e4e4e4;
  --card:#ffffff;
}
*{box-sizing:border-box;margin:0;padding:0}
html,body{width:1200px;height:892px;overflow:hidden}
body{font-family:"Arimo",Arial,sans-serif;background:linear-gradient(#fafafa 0,#f0f0f0 110px,var(--bg) 300px,var(--bg) 100%);color:var(--ink);position:relative}
.site-header{position:absolute;left:149px;top:22px;width:897px;height:86px}
.brand{display:flex;align-items:center;gap:14px;position:absolute;left:0;top:4px}
.brand-dot{width:70px;height:70px;border-radius:50%;background:var(--red)}
.brand-name{font-weight:700;font-size:30px;line-height:32px;color:var(--ink);letter-spacing:.5px}
.contact{position:absolute;right:0;top:0;text-align:right}
.phone{display:flex;align-items:center;justify-content:flex-end;gap:10px;font-size:30px;font-weight:700;color:var(--red-dark)}
.phone svg{width:30px;height:26px}
.address{font-size:15px;line-height:18px;color:#333;margin-top:4px}
.main-nav{position:absolute;left:149px;top:110px;width:897px;height:46px;background:linear-gradient(#3a3a3a,#1c1c1c);border-radius:6px;display:flex;align-items:center;padding-left:10px}
.main-nav a{color:#fff;text-decoration:none;font-size:17px;padding:0 20px;height:46px;line-height:46px;border-right:1px solid #444}
.main-nav a.active{background:var(--red)}
.search{position:absolute;right:10px;top:10px;display:flex}
.search span{width:178px;height:26px;background:#fff;font-size:13px;line-height:26px;padding-left:8px;color:#666;border-radius:3px 0 0 3px}
.search b{width:40px;height:26px;background:var(--red);border-radius:0 3px 3px 0;display:flex;align-items:center;justify-content:center}
.hero{position:absolute;left:149px;top:166px;width:897px;height:297px;background:linear-gradient(135deg,#d2232a,#a3121a);border-radius:10px;box-shadow:0 4px 8px rgba(0,0,0,.3)}
.hero-text{position:absolute;left:22px;top:36px;width:280px;color:#fff}
.hero-text h1{font-size:20px;line-height:24px;font-weight:700;margin-bottom:14px}
.hero-text p{font-size:13px;line-height:16px}
.read-more{position:absolute;left:22px;top:238px;background:linear-gradient(#555,#222);color:#fff;font-size:13px;padding:6px 14px 6px 34px;border-radius:4px}
.read-more:before{content:"";position:absolute;left:10px;top:7px;width:14px;height:14px;border-radius:50%;background:#eee}
.hero-photo{position:absolute;left:326px;top:8px;width:562px;height:281px;border-radius:8px;background:linear-gradient(#4d86c4 0,#a9c8e6 58%,#9a8f72 60%,#6c6552 100%)}
.clients{position:absolute;left:149px;top:497px;width:897px;height:72px;background:#fff;border-radius:6px;box-shadow:0 2px 6px rgba(0,0,0,.25);display:flex;align-items:center}
.clients-tab{width:112px;height:72px;background:linear-gradient(#3a3a3a,#1c1c1c);color:#fff;font-size:17px;line-height:72px;padding-left:14px;border-radius:6px 0 0 6px}
.arrow{width:30px;height:30px;border-radius:50%;background:#ddd;display:flex;align-items:center;justify-content:center;margin:0 10px}
.client-list{flex:1;display:flex;justify-content:space-around;align-items:center}
.client{font-size:19px;font-weight:700;color:var(--ink)}
.panel{position:absolute;top:590px;height:210px;background:var(--card);border-radius:6px;box-shadow:0 2px 6px rgba(0,0,0,.25)}
.panel h2{font-size:16px;font-weight:700;height:42px;line-height:42px;padding-left:44px;border-bottom:1px solid #ddd;position:relative}
.panel h2:before{content:"";position:absolute;left:16px;top:12px;width:18px;height:18px;border-radius:50%;background:var(--red)}
.panel ul{list-style:none;padding:10px 16px}
.panel li{font-size:14px;line-height:34px;padding-left:16px;position:relative;border-bottom:1px dotted #ccc}
.panel li:before{content:"";position:absolute;left:0;top:13px;border-left:7px solid var(--red);border-top:4px solid transparent;border-bottom:4px solid transparent}
.panel li:last-child{border-bottom:0}
.featured{left:149px;width:278px}
.publications{left:446px;width:279px}
.chart{left:763px;width:283px;padding:8px}
.site-footer{position:absolute;left:0;top:816px;width:1200px;height:76px;background:linear-gradient(var(--red),var(--red-dark))}
.footer-nav{position:absolute;left:149px;top:18px;color:#fff;font-size:14px}
.footer-nav span{margin:0 8px}
.copyright{position:absolute;left:149px;top:42px;color:#fff;font-size:13px}
.social{position:absolute;right:154px;top:20px;display:flex;gap:14px}
.social i{width:36px;height:36px;border-radius:50%;background:#7a0a0e}
</style>
</head>
<body>
<header class="site-header">
  <div class="brand">
    <div class="brand-dot"></div>
    <div class="brand-name">PRAIRIE WELLHEAD<br>GEAR DEPOT</div>
  </div>
  <div class="contact">
    <div class="phone">
      <svg viewBox="0 0 30 26"><rect width="30" height="26" rx="5" fill="#c4161c"/><path d="M9 7c2 6 6 10 12 12l2-3-3-2-2 2c-3-1-5-4-6-6l2-2-2-3z" fill="#fff"/></svg>
      555.014.2287
    </div>
    <div class="address">4870 Mesquite Row Suite 214,<br>Plainfield TX 75902</div>
  </div>
</header>

<nav class="main-nav">
  <a href="#">Home</a>
  <a href="#" class="active">About Us</a>
  <a href="#">Services</a>
  <a href="#">Equipment for Sale</a>
  <a href="#">Contact us</a>
  <div class="search"><span>Search</span><b><svg width="14" height="14" viewBox="0 0 14 14"><circle cx="6" cy="6" r="4" fill="none" stroke="#fff" stroke-width="2"/><path d="M9 9l4 4" stroke="#fff" stroke-width="2"/></svg></b></div>
</nav>

<section class="hero">
  <div class="hero-text">
    <h1>Welcome to<br>Prairie Wellhead Gear Depot</h1>
    <p>Lorem Ipsum is simply dummy text of the printing and typesetting industry. Lorem Ipsum has been the industry's standard dummy text ever since the 1500s, when an unknown printer took a galley of type and scrambled it to make a type specimen book. It has survived not only five centuries...</p>
  </div>
  <div class="read-more">Read More</div>
  <div class="hero-photo" role="img" aria-label="Photo of an onshore oil pump jack on open prairie under a blue sky"></div>
</section>

<section class="clients">
  <div class="clients-tab">Our Client</div>
  <div class="arrow"><svg width="10" height="12"><path d="M8 1L2 6l6 5z" fill="#c4161c"/></svg></div>
  <div class="client-list">
    <span class="client">Quellridge</span>
    <span class="client">Fenmarrow</span>
    <span class="client">Zintaro</span>
    <span class="client">Obrelux</span>
    <span class="client">Kestrovane</span>
    <span class="client">Durnwick</span>
  </div>
  <div class="arrow"><svg width="10" height="12"><path d="M2 1l6 5-6 5z" fill="#c4161c"/></svg></div>
</section>

<section class="panel featured">
  <h2>Featured Equipment</h2>
  <ul>
    <li>Fuel Terminal Additives</li>
    <li>Pressure Pumping</li>
    <li>Rotary Steerable Systems</li>
    <li>Steam Generators</li>
  </ul>
</section>

<section class="panel publications">
  <h2>Publications</h2>
  <ul>
    <li>Annual Report 2010-2011</li>
    <li>Investors knowledgebase</li>
    <li>Fast facts and brochures</li>
    <li>Order Reports</li>
  </ul>
</section>

<section class="panel chart">
  <svg width="267" height="194" viewBox="0 0 267 194" font-family="Arimo, Arial, sans-serif" font-size="7" fill="#555">
    <g stroke="#ddd">
      <line x1="26" y1="20" x2="260" y2="20"/><line x1="26" y1="45" x2="260" y2="45"/>
      <line x1="26" y1="70" x2="260" y2="70"/><line x1="26" y1="95" x2="260" y2="95"/>
      <line x1="26" y1="120" x2="260" y2="120"/><line x1="26" y1="145" x2="260" y2="145"/>
    </g>
    <line x1="26" y1="15" x2="26" y2="160" stroke="#999"/>
    <line x1="26" y1="160" x2="260" y2="160" stroke="#999"/>
    <text x="4" y="23">160</text><text x="4" y="48">120</text><text x="4" y="73">80</text><text x="4" y="98">60</text><text x="4" y="123">40</text><text x="4" y="148">20</text>
    <polyline points="50,70 100,52 150,62 200,30 240,82" fill="none" stroke="#6a5aa8" stroke-width="2"/>
    <polyline points="50,92 100,96 150,91 200,88 240,90" fill="none" stroke="#c4161c" stroke-width="2"/>
    <polyline points="50,140 100,138 150,134 200,132 240,130" fill="none" stroke="#8bbf3f" stroke-width="2"/>
    <polyline points="50,146 100,144 150,143 200,140 240,141" fill="none" stroke="#3aa6c8" stroke-width="2"/>
    <text x="42" y="172">Row 1</text><text x="92" y="172">Row 2</text><text x="142" y="172">Row 3</text><text x="192" y="172">Row 4</text>
    <rect x="30" y="182" width="8" height="3" fill="#6a5aa8"/><text x="41" y="186">Column A</text>
    <rect x="86" y="182" width="8" height="3" fill="#c4161c"/><text x="97" y="186">Column B</text>
    <rect x="142" y="182" width="8" height="3" fill="#8bbf3f"/><text x="153" y="186">Column C</text>
    <rect x="198" y="182" width="8" height="3" fill="#3aa6c8"/><text x="209" y="186">Column D</text>
  </svg>
</section>

<footer class="site-footer">
  <div class="footer-nav">Home<span>|</span>About Us<span>|</span>Services<span>|</span>Equipment for Sale<span>|</span>Contact Us</div>
  <div class="copyright">© 2011 Prairie Wellhead Gear Depot. All rights reserved.</div>
  <div class="social" aria-label="Social links"><i></i><i></i><i></i><i></i></div>
</footer>
</body>
</html>
```